Create a memorable Stationary for Security Software Company

TelVandrik is the worldwide leader in securing the Internet. Making Internet communications and critical data secure, reliable and available everywhere has been and continues to be our ongoing vision. We are committed to staying focused on real customer needs and to developing new and innovative security solutions that redefine the security landscape.

Industry/Entity Type

Internet

Font styles to use
Serif
Sans Serif
Script

Colors
0792cd
33a6d7
85cae6

```html
<!DOCTYPE html>
<html lang="en">
<head>
<meta charset="utf-8">
<title>TelVandrik Business Card</title>
<link rel="stylesheet" href="https://fonts.googleapis.com/css2?family=Open+Sans:wght@400;600&display=swap">
<style>
  :root {
    --blue-deep: #0792cd;
    --blue-mid: #33a6d7;
    --blue-light: #85cae6;
    --blue-dark: #0a5f8a;
    --card-face: #eef4f7;
    --page-bg: #d9dee2;
    --contact-text: #e9f5fb;
  }
  html, body {
    margin: 0;
    padding: 0;
    width: 1200px;
    height: 970px;
    overflow: hidden;
    background: var(--page-bg);
    font-family: "Open Sans", sans-serif;
  }
  .card {
    position: absolute;
    left: 100px;
    top: 201px;
    width: 1040px;
    height: 590px;
    transform: scale(0.9615);
    transform-origin: top left;
    border-radius: 30px;
    overflow: hidden;
    background: linear-gradient(160deg, #f7fafc 0%, var(--card-face) 60%, #dfe9ef 100%);
    box-shadow: 0 14px 40px rgba(0, 0, 0, 0.18);
  }
  .card-waves {
    position: absolute;
    inset: 0;
    width: 1040px;
    height: 590px;
  }
  .brand {
    position: absolute;
    left: 78px;
    top: 215px;
    display: flex;
    align-items: center;
    gap: 14px;
  }
  .brand-dot {
    width: 34px;
    height: 34px;
    border-radius: 50%;
    background: var(--blue-mid);
  }
  .brand-name {
    font-size: 48px;
    font-weight: 600;
    color: var(--blue-mid);
    line-height: 1;
  }
  .holder {
    position: absolute;
    right: 42px;
    top: 86px;
    text-align: right;
  }
  .holder-name {
    font-size: 35px;
    font-weight: 600;
    color: var(--blue-dark);
    line-height: 1.1;
  }
  .holder-title {
    font-size: 27px;
    color: var(--blue-mid);
    line-height: 1.2;
  }
  .address {
    position: absolute;
    right: 42px;
    top: 352px;
    text-align: right;
    font-size: 27px;
    line-height: 40px;
    color: var(--contact-text);
  }
  .contacts {
    position: absolute;
    right: 42px;
    top: 437px;
    margin: 0;
    padding: 0;
    list-style: none;
    font-size: 27px;
    line-height: 40px;
    color: var(--contact-text);
  }
  .contacts li {
    display: flex;
    justify-content: flex-end;
    align-items: center;
    gap: 14px;
  }
  .contact-icon {
    width: 32px;
    height: 32px;
  }
</style>
</head>
<body>
  <div class="card">
    <svg class="card-waves" viewBox="0 0 1040 590" aria-hidden="true">
      <defs>
        <linearGradient id="bandFill" x1="0" y1="0" x2="1" y2="1">
          <stop offset="0" stop-color="#0792cd"/>
          <stop offset="1" stop-color="#0a5f8a"/>
        </linearGradient>
      </defs>
      <path d="M0,420 C220,470 400,420 540,340 C700,255 850,240 985,248 C860,250 740,280 600,360 C440,450 240,490 0,455 Z" fill="#1b7fb3"/>
      <path d="M0,470 C230,520 420,470 600,370 C760,290 900,275 1040,290 L1040,590 L0,590 Z" fill="url(#bandFill)"/>
      <path d="M0,505 C260,540 440,480 620,385 C770,305 900,282 1040,292" fill="none" stroke="#f4f8fb" stroke-width="9"/>
      <path d="M100,540 C320,560 470,480 620,400" fill="none" stroke="#85cae6" stroke-width="6" opacity="0.7"/>
      <path d="M0,440 C180,470 350,430 490,350" fill="none" stroke="#85cae6" stroke-width="10" opacity="0.6"/>
    </svg>

    <div class="brand">
      <span class="brand-dot"></span>
      <span class="brand-name">TelVandrik</span>
    </div>

    <div class="holder">
      <div class="holder-name">Employee Name</div>
      <div class="holder-title">President</div>
    </div>

    <div class="address">
      000 Your Address, 2nd Ste.<br>
      Brenford, Ohio 1234
    </div>

    <ul class="contacts">
      <li>000-000-0000
        <svg class="contact-icon" viewBox="0 0 32 32" aria-label="phone">
          <rect x="1" y="1" width="30" height="30" rx="6" fill="#85cae6" opacity="0.45"/>
          <rect x="10" y="5" width="12" height="22" rx="2" fill="none" stroke="#e9f5fb" stroke-width="2"/>
          <line x1="14" y1="23" x2="18" y2="23" stroke="#e9f5fb" stroke-width="2"/>
        </svg>
      </li>
      <li>hello@telvandrik.com
        <svg class="contact-icon" viewBox="0 0 32 32" aria-label="email">
          <rect x="1" y="1" width="30" height="30" rx="6" fill="#85cae6" opacity="0.45"/>
          <rect x="6" y="9" width="20" height="14" fill="none" stroke="#e9f5fb" stroke-width="2"/>
          <path d="M6,9 L16,17 L26,9" fill="none" stroke="#e9f5fb" stroke-width="2"/>
        </svg>
      </li>
      <li>www.telvandrik.com
        <svg class="contact-icon" viewBox="0 0 32 32" aria-label="website">
          <rect x="1" y="1" width="30" height="30" rx="6" fill="#85cae6" opacity="0.45"/>
          <circle cx="16" cy="16" r="9" fill="none" stroke="#e9f5fb" stroke-width="2"/>
          <ellipse cx="16" cy="16" rx="4" ry="9" fill="none" stroke="#e9f5fb" stroke-width="1.5"/>
          <line x1="7" y1="16" x2="25" y2="16" stroke="#e9f5fb" stroke-width="1.5"/>
        </svg>
      </li>
    </ul>
  </div>
</body>
</html>
```